Brisel Home Care Brochure for Recruiting Clients

I need a brochure made for a home care company called 'Brisel Home Care'. I have uploaded the logo, location, and a few items about our company and what it offers. The final design should communicate trust and respect for patients and their families. I will probably be changing the phone number in the next few days so will need to add a new number and more serving locations.

Industry/Entity Type

Home Health Care

Colors
0555a3
ffffff
3176b5
85acd3
0392cd

Requirements
Must have
• Hello All,
• Thank you kindly for your patience. Please add the changes below to the brochures:
• Phone number: 571-555-0143
• Email: briselhc@quorvamail.com
• Homepage: [Non image link removed]Service Locations: Arlington County, Fairfax County, Fauquier County, Loudoun County, Prince William County
• Also please note the additional sentence at the end of the following key points:
• ABOUT US:
• Brisel serves to give patients the personal care they need in order for them to continue to live dignified and independent lives in the comfort of their homes. We begin by assessing and understanding our patient’s individual needs and met those needs through selectively assigning qualified, trustworthy and compassionate home care aids. Brisel holds great pride in keeping our client’s health, quality of life and well-being central in the design and delivery of our services. Our services can prevent re-hospitalization, postpone institutionalization, and reduce the need for urgent care.
• ABOUT OUR SERVICE PROVIDERS:
• We go through a rigorous in-depth application process with all of our service providers, so that you can rest assure that your home care provider is most qualified to meet your needs. Our application process also includes a thorough screening, criminal background check, DMV driving history and a comprehensive exam. Our service providers are trained, monitored, and tested continuously to meet our high standards of work ethic and professionalism. Our care providers are covered by professional liability, bonding, and workers’ compensation insurance. At Brisel teamwork among members is of key importance and it is how we conduct our day to day business. We work as a team with family, patient and their provider in developing an ideal care plan for the patient.
• OUR SERVICES:
• Companionship Services Include:
• - Offer companionship and conversation - Supervise home maintenance
• - Mail bills and letters
• - Provide reminders for appointments
• - Arrange appointments
• - Maintain calendar
• - Plan visits, outings and trips
• - Visit friends
• - Prepare grocery list
• - Assist with clothing selection
• - Stimulate mental awareness
• - Aid with reading
• - Monitor diet and eating
• - Check food expirations
• - Assist with morning and wake-up
• - Assist with evening and tuck-in
• - Provide respite care
• - Provide medication reminders
• - Assist with walking
• - Write letters and correspondence
• - Organize mail
• - Care for house plants
• - Answer the door
• - Assist with entertaining
• - Play games and cards
• - Rent and play movies
• - Oversee home deliveries
• - Supervise home maintenance
• - Discuss current and historical events - Reminisce about the past
• Home Helper Services Include:
• - Assist with laundry and ironing
• - Organize and clean closets
• - Assist with pet care
• - Attend social and sporting events - Accompany to lunch or dinner
• - Care for Alzhiemers
• - Change linens
• - Dust furniture
• - Drop off and pick up dry cleaning
• - Escort for shopping and errands
• - Escort to appointments
• - Escort to religious services
• - Help with airport task
• - Pick up prescriptions
• - Make beds
• - Prepare meals
• - Plan, prepare, and clean-up meals - Prepare future meals
• - Provide light housekeeping
• - Take out garbage
• Personal Services Include:
• - Ambulation
• - Bathing
• - Cognitive impairment - Mobility
• - Transferring
• - Incontinence
• - Dressing
• - Eating
• - Grooming
Nice to have
• Nice pictures of elderly clients with helpers or nurse.

```html
<!DOCTYPE html>
<html lang="en">
<head>
<meta charset="utf-8">
<title>Brisel Home Care – Brochure</title>
<link rel="stylesheet" href="https://fonts.googleapis.com/css2?family=Fira+Sans:ital,wght@0,400;0,500;1,300&family=Fira+Sans+Condensed:wght@400&display=swap">
<style>
  :root{
    --navy:#1b4f80;
    --navy-deep:#174672;
    --mid-blue:#3f7db3;
    --light-blue:#85acd3;
    --white:#ffffff;
    --page:#f1f1f1;
    --services-box:rgba(27,79,128,.93);
  }
  *{box-sizing:border-box;margin:0;padding:0}
  html,body{width:1200px;height:602px;overflow:hidden;background:var(--page)}
  body{position:relative;font-family:"Fira Sans",sans-serif;color:var(--white)}

  .spread{position:absolute;top:81px;width:558px;height:433px;overflow:hidden;box-shadow:0 3px 8px rgba(0,0,0,.25)}
  .spread--outside{left:30px}
  .spread--inside{left:612px}

  .panel{position:absolute}
  .about{left:0;top:0;width:186px;height:433px;background:var(--navy);padding:36px 15px 0 31px}
  .about h2{font-weight:400;font-size:16px;margin-bottom:13px}
  .about p{font-size:10.2px;line-height:12.6px;margin-bottom:12px}

  .photo{position:absolute}
  .photo--carer{left:186px;top:0;width:186px;height:146px;background:linear-gradient(135deg,#f4f1ee 0%,#e8d9cc 45%,#b98a62 80%,#d9c2a8 100%)}
  .photo--pair{left:372px;top:146px;width:186px;height:287px;background:linear-gradient(160deg,#f3f1ef 0%,#e9ddd0 40%,#c9b39a 70%,#b9c9dc 100%)}

  .location{left:186px;top:146px;width:186px;height:287px;background:var(--mid-blue);padding:30px 12px 0 32px}
  .location h2{font-weight:400;font-size:16px;margin-bottom:8px}
  .location p{font-size:9.6px;line-height:12px}
  .location .call{margin-top:10px}
  .location .phone{font-size:16px;line-height:19px}
  .location .email{font-size:9.6px}
  .location .brand{position:absolute;left:30px;bottom:20px}

  .cover{left:372px;top:0;width:186px;height:146px;background:var(--navy)}
  .cover .brand{position:absolute;left:34px;top:36px}
  .cover .tagline{position:absolute;left:41px;top:100px;font-style:italic;font-weight:300;font-size:11px}

  .brand{display:flex;align-items:center;gap:7px}
  .brand-mark{width:26px;height:26px;background:var(--white);border-radius:3px}
  .brand-name{font-weight:400;line-height:1}
  .cover .brand-name{font-size:17px;line-height:19px}
  .cover .brand-mark{width:32px;height:32px}
  .location .brand-name{font-size:13px;line-height:14.5px}

  .photo--team{left:0;top:0;width:558px;height:433px;background:linear-gradient(100deg,#4a2a1c 0%,#6b4330 30%,#b06b7a 55%,#7d5b4a 75%,#3f3a3e 100%)}

  .providers{left:21px;top:40px;width:126px}
  .providers h2{font-weight:400;font-size:15px;line-height:16.5px;margin-bottom:10px}
  .providers p{font-family:"Fira Sans Condensed",sans-serif;font-size:7.3px;line-height:8.9px;margin-bottom:8px}

  .services{left:322px;top:42px;width:236px;height:359px;background:var(--services-box);padding:12px 6px 0 14px}
  .services h2{font-weight:400;font-size:14px;margin-bottom:3px}
  .services-cols{display:flex;gap:8px}
  .services-col{width:110px}
  .services-col + .services-col{width:100px}
  .service-group{font-family:"Fira Sans Condensed",sans-serif;font-size:6.7px;line-height:9px;list-style:none}
  .group-title{font-family:"Fira Sans Condensed",sans-serif;font-size:6.7px;line-height:9px}
  .group-title--spaced{margin-top:9px}
</style>
</head>
<body>

<section class="spread spread--outside">
  <div class="panel about">
    <h2>About Us</h2>
    <p>Brisel serves to give patients the personal care they need in order for them to continue to live dignified and independent lives in the comfort of their homes.</p>
    <p>We begin by assessing and understanding our patient’s individual needs and met those needs through selectively assigning qualified, trustworthy and compassionate home care aids. Brisel holds great pride in keeping our client’s health, quality of life and well-being central in the design and delivery of our services. Our services can prevent re-hospitalization, postpone institutionalization, and reduce the need for urgent care.</p>
  </div>

  <div class="photo photo--carer" role="img" aria-label="Smiling senior woman seated while a young caregiver leans over her shoulder"></div>

  <div class="panel location">
    <h2>Location</h2>
    <p>318 Hollin Crest Lane,<br>Falls Church, VA 22046<br>Serving the following counties:<br>Arlington County, Fairfax County,<br>Fauquier County, Loudoun County,<br>Prince William County</p>
    <p class="call">Call us now at</p>
    <p class="phone">571-555-0143</p>
    <p class="email">briselhc@quorvamail.com</p>
    <div class="brand">
      <span class="brand-mark"></span>
      <span class="brand-name">Brisel<br>Home<br>Care</span>
    </div>
  </div>

  <div class="panel cover">
    <div class="brand">
      <span class="brand-mark"></span>
      <span class="brand-name">Brisel<br>Home<br>Care</span>
    </div>
    <p class="tagline">Trust the professionals</p>
  </div>

  <div class="photo photo--pair" role="img" aria-label="Senior woman and young caregiver smiling together, cheek to cheek"></div>
</section>

<section class="spread spread--inside">
  <div class="photo photo--team" role="img" aria-label="Caregiver and elderly woman sharing a warm moment at home, folding laundry together"></div>

  <div class="panel providers">
    <h2>About our<br>service providers</h2>
    <p>We go through a rigorous in-depth application process with all of our service providers, so that you can rest assure that your home care provider is most qualified to meet your needs. Our application process also includes a thorough screening, criminal background check, DMV driving history and a comprehensive exam.</p>
    <p>Our service providers are trained, monitored, and tested continuously to meet our high standards of work ethic and professionalism. Our care providers are covered by professional liability, bonding, and workers’ compensation insurance. At Brisel teamwork among members is of key importance and it is how we conduct our day to day business. We work as a team with family, patient and their provider in developing an ideal care plan for the patient.</p>
  </div>

  <div class="panel services">
    <h2>Our services</h2>
    <div class="services-cols">
      <div class="services-col">
        <p class="group-title">Companionship Services Include:</p>
        <ul class="service-group">
          <li>-Offer companionship and conversation</li>
          <li>-Supervise home maintenance</li>
          <li>-Mail bills and letters</li>
          <li>-Provide reminders for appointments</li>
          <li>-Arrange appointments</li>
          <li>-Maintain calendar</li>
          <li>-Plan visits, outings and trips</li>
          <li>-Visit friends</li>
          <li>-Prepare grocery list</li>
          <li>-Assist with clothing selection</li>
          <li>-Stimulate mental awareness</li>
          <li>-Aid with reading</li>
          <li>-Monitor diet and eating</li>
          <li>-Check food expirations</li>
          <li>-Assist with morning and wake-up</li>
          <li>-Assist with evening and tuck-in</li>
          <li>-Provide respite care</li>
          <li>-Provide medication reminders</li>
          <li>-Assist with walking</li>
          <li>-Write letters and correspondence</li>
          <li>-Organize mail</li>
          <li>-Care for house plants</li>
          <li>-Answer the door</li>
          <li>-Assist with clothing selection</li>
          <li>-Assist with entertaining</li>
          <li>-Play games and cards</li>
          <li>-Rent and play movies</li>
          <li>-Oversee home deliveries</li>
          <li>-Supervise home maintenance</li>
          <li>-Discuss current and historical events</li>
          <li>-Reminisce about the past</li>
        </ul>
      </div>
      <div class="services-col">
        <p class="group-title">Home Helper Services Include:</p>
        <ul class="service-group">
          <li>-Assist with laundry and ironing</li>
          <li>-Organize and clean closets</li>
          <li>-Assist with pet care</li>
          <li>-Attend social and sporting events</li>
          <li>-Accompany to lunch or dinner</li>
          <li>-Care for Alzhiemers</li>
          <li>-Change linens</li>
          <li>-Dust furniture</li>
          <li>-Drop off and pick up dry cleaning</li>
          <li>-Escort for shopping and errands</li>
          <li>-Escort to appointments</li>
          <li>-Escort to religious services</li>
          <li>-Help with airport task</li>
          <li>-Pick up prescriptions</li>
          <li>-Make beds</li>
          <li>-Prepare meals</li>
          <li>-Plan, prepare, and clean-up meals</li>
          <li>-Prepare future meals</li>
          <li>-Provide light housekeeping</li>
          <li>-Take out garbage</li>
        </ul>
        <p class="group-title group-title--spaced">Personal Services Include:</p>
        <ul class="service-group">
          <li>-Ambulation</li>
          <li>-Bathing</li>
          <li>-Cognitive impairment</li>
          <li>-Mobility</li>
          <li>-Transferring</li>
          <li>-Incontinence</li>
          <li>-Dressing</li>
          <li>-Eating</li>
          <li>-Grooming</li>
        </ul>
      </div>
    </div>
  </div>
</section>

</body>
</html>
```